Buch-/eBook-Cover für ein Fantasy Roman
Zielgruppe
Meine Zielgruppe sind Jugendliche und junge Erwachsene, aber auch für Ältere könnte mein Buch interessant sein.
Aufgabenstellung
Bei meinem Buch handelt es sich um einen Fantasy Roman. Es heißt 'Wanderlicht - Mut kommt nie allein' und der Autor ist Greta Obermühler.
Das Buch handelt von einem Mädchen, welches eigentlich ein ganz normales Leben führt, aber dieses durch eine Pressekonferenz vom Präsidenten komplett durcheinander gerät. Denn viele Menschen sollen an einem Virus leiden. Die Menschen sollen sich aber keine Sorgen machen. Doch alles läuft durcheinander, da die infizierten Menschen einer nach dem anderen spurlos verschwinden.
Auf meinem Cover soll keine Figur zu sehen sein. Ich hätte gerne ein Zusammenspiel zwischen den Farben Blau und Grün. sie sollen harmonisch und fließend ineinander übergehen. Auch etwas Glitzer für etwas Geheimnisvolles darf auf dem Cover sein. Den Titel hätte ich gerne in der Mitte. Wo der Autorname stehen soll, bin ich offen.

```html
<!DOCTYPE html>
<html lang="de">
<head>
<meta charset="utf-8">
<title>Wanderlicht – Buchcover</title>
<link rel="stylesheet" href="https://fonts.googleapis.com/css2?family=Bebas+Neue&family=Oswald:wght@500&family=Uncial+Antiqua&display=swap">
<style>
  :root {
    --deep-navy: #0a2a6e;
    --royal-blue: #1c5fb4;
    --mist-cyan: #56d0cf;
    --teal: #1f9a8a;
    --leaf-green: #2fa83a;
    --lime: #7fb52a;
    --forest-dark: #031a12;
    --sparkle: #b8ffd0;
    --text: #ffffff;
  }
  html, body {
    margin: 0;
    padding: 0;
    overflow: hidden;
    background: #000;
  }
  .cover {
    position: relative;
    width: 750px;
    height: 1200px;
    overflow: hidden;
    color: var(--text);
    background:
      radial-gradient(ellipse 260px 220px at 300px 250px, rgba(86,208,207,0.85), transparent 70%),
      radial-gradient(ellipse 300px 380px at 640px 420px, rgba(127,181,42,0.75), transparent 70%),
      radial-gradient(ellipse 380px 420px at 560px 800px, rgba(47,168,58,0.85), transparent 70%),
      radial-gradient(ellipse 320px 500px at 40px 650px, rgba(28,95,180,0.95), transparent 75%),
      radial-gradient(ellipse 260px 360px at 30px 950px, var(--deep-navy), transparent 75%),
      linear-gradient(180deg, transparent 60%, var(--forest-dark) 100%),
      linear-gradient(100deg, var(--royal-blue) 0%, var(--teal) 45%, var(--leaf-green) 100%);
  }
  .cover__sparkles {
    position: absolute;
    inset: 0;
    width: 750px;
    height: 1200px;
  }
  .cover__sparkles circle { fill: var(--sparkle); }
  .cover__author {
    position: absolute;
    top: 52px;
    left: 0;
    width: 100%;
    text-align: center;
    font-family: "Bebas Neue", sans-serif;
    font-size: 52px;
    letter-spacing: 1px;
    line-height: 1;
    margin: 0;
  }
  .cover__title {
    position: absolute;
    top: 460px;
    left: 0;
    width: 100%;
    text-align: center;
    font-family: "Uncial Antiqua", serif;
    font-weight: 400;
    font-size: 98px;
    line-height: 1;
    margin: 0;
  }
  .cover__subtitle {
    position: absolute;
    top: 632px;
    left: 0;
    width: 100%;
    text-align: center;
    font-family: "Oswald", sans-serif;
    font-weight: 500;
    font-size: 42px;
    line-height: 53px;
    text-transform: uppercase;
    margin: 0;
  }
</style>
</head>
<body>
  <main class="cover">
    <svg class="cover__sparkles" viewBox="0 0 750 1200" aria-hidden="true">
      <circle cx="250" cy="310" r="1.6" opacity=".6"/>
      <circle cx="320" cy="380" r="1.2" opacity=".5"/>
      <circle cx="410" cy="350" r="1.4" opacity=".5"/>
      <circle cx="180" cy="520" r="1.3" opacity=".5"/>
      <circle cx="120" cy="640" r="1.5" opacity=".4"/>
      <circle cx="560" cy="520" r="1.8" opacity=".6"/>
      <circle cx="600" cy="600" r="1.4" opacity=".6"/>
      <circle cx="650" cy="660" r="2" opacity=".7"/>
      <circle cx="700" cy="720" r="1.5" opacity=".6"/>
      <circle cx="620" cy="760" r="1.8" opacity=".7"/>
      <circle cx="540" cy="790" r="1.3" opacity=".6"/>
      <circle cx="480" cy="820" r="1.6" opacity=".7"/>
      <circle cx="420" cy="850" r="1.2" opacity=".6"/>
      <circle cx="580" cy="870" r="2.2" opacity=".8"/>
      <circle cx="660" cy="880" r="1.5" opacity=".6"/>
      <circle cx="520" cy="910" r="1.8" opacity=".7"/>
      <circle cx="450" cy="930" r="1.3" opacity=".5"/>
      <circle cx="380" cy="900" r="1.5" opacity=".5"/>
      <circle cx="340" cy="820" r="1.2" opacity=".5"/>
      <circle cx="290" cy="760" r="1.4" opacity=".5"/>
      <circle cx="210" cy="780" r="1.2" opacity=".4"/>
      <circle cx="560" cy="960" r="1.6" opacity=".6"/>
      <circle cx="630" cy="980" r="1.3" opacity=".5"/>
      <circle cx="500" cy="1000" r="1.4" opacity=".5"/>
      <circle cx="700" cy="820" r="1.2" opacity=".5"/>
      <circle cx="690" cy="560" r="1.4" opacity=".5"/>
      <circle cx="470" cy="720" r="1.5" opacity=".6"/>
      <circle cx="400" cy="760" r="1.2" opacity=".5"/>
      <circle cx="150" cy="410" r="1.3" opacity=".4"/>
      <circle cx="360" cy="280" r="1.1" opacity=".5"/>
      <circle cx="600" cy="1050" r="1.2" opacity=".4"/>
      <circle cx="250" cy="880" r="1.2" opacity=".4"/>
    </svg>

    <p class="cover__author">Greta Obermühler</p>
    <h1 class="cover__title">Wanderlicht</h1>
    <p class="cover__subtitle">Mut kommt<br>nie allein</p>
  </main>
</body>
</html>
```